Gin Bottle label

Hi, I would like a design based on a traditional, Vintage, Victorian type label.
The product is 'Hawthorn & Sloeberry Gin'
It will be 50cl and 40% vol.
The Gin will be dark brown in colour and attached is the types of bottle and a few ideas of the styles I like.
Many Thanks

```html
<!DOCTYPE html>
<html lang="en">
<head>
<meta charset="utf-8">
<title>Hawthorn &amp; Sloeberry Gin – Label</title>
<link rel="stylesheet" href="https://fonts.googleapis.com/css2?family=Zilla+Slab:wght@600;700&family=Fira+Sans+Condensed:wght@500&display=swap">
<style>
  :root {
    --canvas-bg: #ffffff;
    --label-cream: #ecdcb8;
    --label-edge: #c8b287;
    --ink-maroon: #7d0c3c;
    --ink-rose: #a3506a;
    --ornament-tone: #8a7078;
  }
  html, body {
    margin: 0;
    padding: 0;
    width: 1000px;
    height: 1200px;
    overflow: hidden;
    background: var(--canvas-bg);
  }
  .label-canvas {
    display: block;
    width: 1000px;
    height: 1200px;
  }
  .label-shape { fill: var(--label-cream); stroke: var(--label-edge); stroke-width: 2; }
  .label-keyline { fill: none; stroke: var(--label-edge); stroke-width: 1.5; }
  .category-name {
    font-family: "Zilla Slab", Georgia, serif;
    font-weight: 700;
    font-size: 50px;
    fill: var(--ink-rose);
  }
  .category-marker { fill: none; stroke: var(--ink-rose); stroke-width: 3.5; }
  .product-name {
    font-family: "Zilla Slab", Georgia, serif;
    font-weight: 700;
    font-size: 100px;
    fill: var(--ink-maroon);
  }
  .volume-info {
    font-family: "Fira Sans Condensed", Arial, sans-serif;
    font-weight: 500;
    font-size: 22px;
    fill: var(--ink-rose);
  }
  .volume-marker { fill: none; stroke: var(--ink-rose); stroke-width: 3; }
  .ornament-area { fill: var(--ornament-tone); opacity: 0.55; }
</style>
</head>
<body>
<svg class="label-canvas" viewBox="0 0 1000 1200" xmlns="http://www.w3.org/2000/svg">
  <!-- label body -->
  <polygon class="label-shape" points="500,180 920,600 500,1020 80,600"/>
  <polygon class="label-keyline" points="500,192 908,600 500,1008 92,600"/>

  <!-- top flourish -->
  <rect class="ornament-area" x="458" y="240" width="84" height="68" rx="26" role="img" aria-label="Victorian scroll flourish ornament"/>

  <!-- category line -->
  <rect class="category-marker" x="0" y="0" width="11" height="11" transform="translate(397 346) rotate(45)"/>
  <rect class="category-marker" x="0" y="0" width="11" height="11" transform="translate(422 346) rotate(45)"/>
  <text class="category-name" x="500" y="364" text-anchor="middle">GIN</text>
  <rect class="category-marker" x="0" y="0" width="11" height="11" transform="translate(578 346) rotate(45)"/>
  <rect class="category-marker" x="0" y="0" width="11" height="11" transform="translate(603 346) rotate(45)"/>

  <!-- flourish under category -->
  <rect class="ornament-area" x="332" y="380" width="336" height="64" rx="32" role="img" aria-label="Victorian scroll flourish ornament"/>

  <!-- side flourishes -->
  <rect class="ornament-area" x="180" y="548" width="44" height="104" rx="18" role="img" aria-label="Victorian scroll flourish ornament, left side"/>
  <rect class="ornament-area" x="776" y="548" width="44" height="104" rx="18" role="img" aria-label="Victorian scroll flourish ornament, right side"/>

  <!-- product name -->
  <text class="product-name" x="500" y="598" text-anchor="middle" textLength="520" lengthAdjust="spacingAndGlyphs">HAWTHORN</text>
  <text class="product-name" x="500" y="690" text-anchor="middle" textLength="520" lengthAdjust="spacingAndGlyphs">&amp; SLOEBERRY</text>

  <!-- flourish above volume -->
  <rect class="ornament-area" x="332" y="748" width="336" height="64" rx="32" role="img" aria-label="Victorian scroll flourish ornament"/>

  <!-- volume and strength -->
  <rect class="volume-marker" x="0" y="0" width="10" height="10" transform="translate(398 848) rotate(45)"/>
  <text class="volume-info" x="450" y="864" text-anchor="middle">50 CL</text>
  <rect class="volume-marker" x="0" y="0" width="10" height="10" transform="translate(500 848) rotate(45)"/>
  <text class="volume-info" x="550" y="864" text-anchor="middle">40 %</text>
  <rect class="volume-marker" x="0" y="0" width="10" height="10" transform="translate(602 848) rotate(45)"/>

  <!-- bottom flourish -->
  <rect class="ornament-area" x="458" y="892" width="84" height="64" rx="26" role="img" aria-label="Victorian scroll flourish ornament"/>
</svg>
</body>
</html>
```